Face cream packaging | Cosmetic start-up

This project is about creating design proposals for two different types of packaging. Once to a cream jar made of glass and once to a jar made of plastic.
Three different designs must be created for each type of jar. Later, the different packaging will be used as customization options in an online store for cosmetics.

- The packaging variant made of glass should have color gradients. Three different shades are to be chosen. (Preferably with the primary colors red, blue and green). Note: The designer can create other proposals at will if he has better ideas. The logo must be included in some form. (Link to manufacturer description: https://catalogue.vorelpackwerk.com/en/portals/vorelpackwerk/assets/48302915/lio-50-ml/)

- With the plastic type of packaging, the designer has a lot of freedom to design. The only requirement is that the design must be artistic. It doesn't matter whether abstract patterns, geometric figures, mandalas or just a basic color is chosen. The main thing is that the packaging inspires. The logo must be included in some form. (Link to manufacturer description: https://catalogue.vorelpackwerk.com/en/portals/vorelpackwerk/assets/48302922/tova-50-ml/)

Thank you in advance for your work and best regards
Ubel

Target Market(s)

Young people with an affinity for social media and the web. Focus is on the female clientele.

Industry/Entity Type

Cosmetics

Font styles to use
Script

Colors
eea4c8
f59195
85cae6
cadf82

Requirements
Must have
• The logo must be included in some form. (PNG-File attached)
Nice to have
• Other types of packaging (can shape, packaging material)

```html
<!DOCTYPE html>
<html lang="en">
<head>
<meta charset="utf-8">
<title>Sola Vie – Cream Label Proposals</title>
<link rel="stylesheet" href="https://fonts.googleapis.com/css2?family=Montserrat:wght@400;600;700;800&family=Josefin+Sans:wght@300&display=swap">
<style>
  :root {
    --stage: #3b3b3d;
    --variant-letter: #c4c4c4;
    --ink-light: #ffffff;
    --ink-dark: #161616;
    --green: #22b14c;
    --lime: #b5d334;
    --yellow: #fce30f;
    --violet: #4b3596;
    --magenta: #b02f8f;
    --red: #e2202b;
    --rose-brown: #b24f5d;
    --teal: #14a596;
    --blue: #1477c2;
    --deep-teal: #127a78;
    --mint: #a2dcc3;
  }
  * { box-sizing: border-box; margin: 0; padding: 0; }
  html, body { width: 1200px; height: 1086px; overflow: hidden; background: var(--stage); }
  body { position: relative; font-family: "Montserrat", sans-serif; }

  .variant-letter {
    position: absolute; left: 52px; width: 60px; text-align: center;
    font-family: "Montserrat", sans-serif; font-weight: 400; font-size: 82px;
    color: var(--variant-letter); line-height: 1;
  }

  .label {
    position: absolute; left: 148px; width: 988px; height: 198px;
    overflow: hidden; color: var(--ink-light);
  }
  .label--a { top: 96px;
    background:
      radial-gradient(ellipse 30% 80% at 43% 20%, rgba(255,232,10,.95), rgba(255,232,10,0) 100%),
      linear-gradient(90deg, var(--green) 0%, #8cc63f 22%, #f2e21a 40%, var(--yellow) 55%, #d9dc22 72%, var(--lime) 86%, var(--green) 100%); }
  .label--b { top: 328px;
    background: linear-gradient(180deg, var(--violet) 0%, #7a2f94 28%, var(--magenta) 55%, #cf2f5e 75%, var(--red) 100%); }
  .label--c { top: 560px;
    background:
      radial-gradient(ellipse 22% 60% at 62% 100%, rgba(20,119,194,.9), rgba(20,119,194,0) 100%),
      linear-gradient(90deg, var(--rose-brown) 0%, #3c8f99 22%, var(--teal) 42%, #1592b0 58%, var(--blue) 66%, #1799ae 82%, var(--rose-brown) 100%); }
  .label--d { top: 792px;
    background:
      radial-gradient(ellipse 45% 70% at 45% 50%, var(--mint), rgba(162,220,195,0) 100%),
      linear-gradient(90deg, var(--deep-teal) 0%, #5fb5a3 30%, var(--mint) 50%, #6ebfab 72%, var(--deep-teal) 100%); }

  .label__copy {
    position: absolute; left: 34px; top: 24px; width: 262px;
    font-size: 8.1px; line-height: 12px; letter-spacing: -0.12px;
    text-align: justify; font-weight: 400;
  }
  .label__code-box { position: absolute; left: 34px; top: 129px; width: 102px; height: 54px; background: var(--ink-light); }
  .label--d .label__code-box { background: #050505; }

  .brand-name {
    position: absolute; left: 388px; top: 62px; width: 220px; text-align: center;
    font-family: "Josefin Sans", sans-serif; font-weight: 300; font-size: 34px;
    letter-spacing: 1px; line-height: 1;
  }
  .brand-rule { position: absolute; left: 421px; top: 114px; width: 169px; height: 1px; background: var(--ink-light); }
  .product-type {
    position: absolute; left: 400px; top: 138px; width: 180px; text-align: center;
    font-family: "Josefin Sans", sans-serif; font-weight: 300; font-size: 19px; letter-spacing: 3px;
  }
  .label--d .brand-name, .label--d .product-type { color: var(--ink-dark); }
  .label--d .brand-rule { background: var(--ink-dark); }

  .facts {
    position: absolute; left: 724px; top: 17px; width: 221px; height: 129px;
    border: 1px solid var(--ink-light); padding: 1px 2px; overflow: hidden;
  }
  .facts > * { display: block; }
  .facts__title { font-weight: 800; font-size: 10.6px; line-height: 13px; letter-spacing: -0.3px; white-space: nowrap; }
  .facts__meta { font-size: 5px; line-height: 6px; font-weight: 600; white-space: nowrap; }
  .facts__meta--small { font-size: 3.8px; line-height: 5px; font-weight: 700; }
  .facts__row { display: flex; justify-content: space-between; font-size: 4.8px; line-height: 6px; white-space: nowrap; }
  .facts__row--bold { font-weight: 700; }
  .facts__row--serving { font-size: 5.4px; line-height: 7px; font-weight: 700; border-bottom: 3px solid var(--ink-light); }
  .facts__row--calories { font-size: 10px; line-height: 12px; font-weight: 800; border-bottom: 2px solid var(--ink-light); }
  .facts__row--line { border-bottom: 0.5px solid var(--ink-light); }
  .facts__row--indent { padding-left: 6px; font-weight: 400; }
  .facts__dv { font-size: 3.8px; line-height: 5px; font-weight: 700; text-align: right; }
  .facts__note { font-size: 3.6px; line-height: 4.4px; margin-top: 1px; }

  .label__tagline { position: absolute; left: 726px; top: 152px; width: 260px; font-size: 7.6px; line-height: 9.8px; }
</style>
</head>
<body>

<div class="variant-letter" style="top:172px">A</div>
<div class="variant-letter" style="top:404px">B</div>
<div class="variant-letter" style="top:636px">C</div>
<div class="variant-letter" style="top:868px">D</div>

<!-- Label A -->
<section class="label label--a">
  <p class="label__copy">Lorem ipsum dolor sit amet, consectetuer adipiscing elit, sed diam nonummy nibh euismod tincidunt ut laoreet dolore magna aliquam erat volutpat. Ut wisi enim ad minim veniam, quis nostrud exerci tation ullamcorper suscipit lobortis nisl ut aliquip ex ea commodo consequat. Duis autem vel eum iriure dolor in hendrerit in vulputate velit esse molestie consequat, vel illum dolore eu feugiat nulla facilisis at vero eros et luptatum zzril delenit augue duis dolore te feugait nulla facilisi.</p>
  <div class="label__code-box"></div>
  <div class="brand-name">Sola Vie</div>
  <div class="brand-rule"></div>
  <div class="product-type">CREAM</div>
  <div class="facts">
    <div class="facts__title">Nutrition Facts/Datos de Nutrición</div>
    <div class="facts__meta">4 servings per container/4 raciones por envase</div>
    <div class="facts__row facts__row--serving"><span>Serving size/Tamaño de la porción</span><span>1 cup/1 taza (180g)</span></div>
    <div class="facts__meta facts__meta--small">Amount per serving/Cantidad por porción</div>
    <div class="facts__row facts__row--calories"><span>Calories/Calorías</span><span>245</span></div>
    <div class="facts__dv">% Daily Value*/% Valor diario*</div>
    <div class="facts__row facts__row--line facts__row--bold"><span>Total Fat/Grasa total 12g</span><span>14%</span></div>
    <div class="facts__row facts__row--line facts__row--indent"><span>Saturated Fat/Grasa Saturada 2g</span><span>10%</span></div>
    <div class="facts__row facts__row--line facts__row--indent"><span>Trans Fat/Grasa Trans 0g</span><span></span></div>
    <div class="facts__row facts__row--line facts__row--bold"><span>Cholesterol/Colesterol 8mg</span><span>3%</span></div>
    <div class="facts__row facts__row--line facts__row--bold"><span>Sodium/Sodio 210mg</span><span>9%</span></div>
    <div class="facts__row facts__row--line facts__row--bold"><span>Total Carbohydrate/Carbohidrato Total 34g</span><span>12%</span></div>
    <p class="facts__note">*The % Daily Value (DV) tells you how much a nutrient in a serving of food adds to a daily diet. 2,000 calories a day is used for general advice.</p>
    <p class="facts__note">*El % Valor Diario indica cuánto aporta un nutriente de una porción a una dieta diaria de 2,000 calorías.</p>
  </div>
  <p class="label__tagline">Lorem ipsum amet, consectetuer adipiscing elit,<br>tincidunt ut laoreet dolore magna aliquam erat volutpat.</p>
</section>

<!-- Label B -->
<section class="label label--b">
  <p class="label__copy">Lorem ipsum dolor sit amet, consectetuer adipiscing elit, sed diam nonummy nibh euismod tincidunt ut laoreet dolore magna aliquam erat volutpat. Ut wisi enim ad minim veniam, quis nostrud exerci tation ullamcorper suscipit lobortis nisl ut aliquip ex ea commodo consequat. Duis autem vel eum iriure dolor in hendrerit in vulputate velit esse molestie consequat, vel illum dolore eu feugiat nulla facilisis at vero eros et luptatum zzril delenit augue duis dolore te feugait nulla facilisi.</p>
  <div class="label__code-box"></div>
  <div class="brand-name">Sola Vie</div>
  <div class="brand-rule"></div>
  <div class="product-type">CREAM</div>
  <div class="facts">
    <div class="facts__title">Nutrition Facts/Datos de Nutrición</div>
    <div class="facts__meta">4 servings per container/4 raciones por envase</div>
    <div class="facts__row facts__row--serving"><span>Serving size/Tamaño de la porción</span><span>1 cup/1 taza (180g)</span></div>
    <div class="facts__meta facts__meta--small">Amount per serving/Cantidad por porción</div>
    <div class="facts__row facts__row--calories"><span>Calories/Calorías</span><span>245</span></div>
    <div class="facts__dv">% Daily Value*/% Valor diario*</div>
    <div class="facts__row facts__row--line facts__row--bold"><span>Total Fat/Grasa total 12g</span><span>14%</span></div>
    <div class="facts__row facts__row--line facts__row--indent"><span>Saturated Fat/Grasa Saturada 2g</span><span>10%</span></div>
    <div class="facts__row facts__row--line facts__row--indent"><span>Trans Fat/Grasa Trans 0g</span><span></span></div>
    <div class="facts__row facts__row--line facts__row--bold"><span>Cholesterol/Colesterol 8mg</span><span>3%</span></div>
    <div class="facts__row facts__row--line facts__row--bold"><span>Sodium/Sodio 210mg</span><span>9%</span></div>
    <div class="facts__row facts__row--line facts__row--bold"><span>Total Carbohydrate/Carbohidrato Total 34g</span><span>12%</span></div>
    <p class="facts__note">*The % Daily Value (DV) tells you how much a nutrient in a serving of food adds to a daily diet. 2,000 calories a day is used for general advice.</p>
    <p class="facts__note">*El % Valor Diario indica cuánto aporta un nutriente de una porción a una dieta diaria de 2,000 calorías.</p>
  </div>
  <p class="label__tagline">Lorem ipsum amet, consectetuer adipiscing elit,<br>tincidunt ut laoreet dolore magna aliquam erat volutpat.</p>
</section>

<!-- Label C -->
<section class="label label--c">
  <p class="label__copy">Lorem ipsum dolor sit amet, consectetuer adipiscing elit, sed diam nonummy nibh euismod tincidunt ut laoreet dolore magna aliquam erat volutpat. Ut wisi enim ad minim veniam, quis nostrud exerci tation ullamcorper suscipit lobortis nisl ut aliquip ex ea commodo consequat. Duis autem vel eum iriure dolor in hendrerit in vulputate velit esse molestie consequat, vel illum dolore eu feugiat nulla facilisis at vero eros et luptatum zzril delenit augue duis dolore te feugait nulla facilisi.</p>
  <div class="label__code-box"></div>
  <div class="brand-name">Sola Vie</div>
  <div class="brand-rule"></div>
  <div class="product-type">CREAM</div>
  <div class="facts">
    <div class="facts__title">Nutrition Facts/Datos de Nutrición</div>
    <div class="facts__meta">4 servings per container/4 raciones por envase</div>
    <div class="facts__row facts__row--serving"><span>Serving size/Tamaño de la porción</span><span>1 cup/1 taza (180g)</span></div>
    <div class="facts__meta facts__meta--small">Amount per serving/Cantidad por porción</div>
    <div class="facts__row facts__row--calories"><span>Calories/Calorías</span><span>245</span></div>
    <div class="facts__dv">% Daily Value*/% Valor diario*</div>
    <div class="facts__row facts__row--line facts__row--bold"><span>Total Fat/Grasa total 12g</span><span>14%</span></div>
    <div class="facts__row facts__row--line facts__row--indent"><span>Saturated Fat/Grasa Saturada 2g</span><span>10%</span></div>
    <div class="facts__row facts__row--line facts__row--indent"><span>Trans Fat/Grasa Trans 0g</span><span></span></div>
    <div class="facts__row facts__row--line facts__row--bold"><span>Cholesterol/Colesterol 8mg</span><span>3%</span></div>
    <div class="facts__row facts__row--line facts__row--bold"><span>Sodium/Sodio 210mg</span><span>9%</span></div>
    <div class="facts__row facts__row--line facts__row--bold"><span>Total Carbohydrate/Carbohidrato Total 34g</span><span>12%</span></div>
    <p class="facts__note">*The % Daily Value (DV) tells you how much a nutrient in a serving of food adds to a daily diet. 2,000 calories a day is used for general advice.</p>
    <p class="facts__note">*El % Valor Diario indica cuánto aporta un nutriente de una porción a una dieta diaria de 2,000 calorías.</p>
  </div>
  <p class="label__tagline">Lorem ipsum amet, consectetuer adipiscing elit,<br>tincidunt ut laoreet dolore magna aliquam erat volutpat.</p>
</section>

<!-- Label D -->
<section class="label label--d">
  <p class="label__copy">Lorem ipsum dolor sit amet, consectetuer adipiscing elit, sed diam nonummy nibh euismod tincidunt ut laoreet dolore magna aliquam erat volutpat. Ut wisi enim ad minim veniam, quis nostrud exerci tation ullamcorper suscipit lobortis nisl ut aliquip ex ea commodo consequat. Duis autem vel eum iriure dolor in hendrerit in vulputate velit esse molestie consequat, vel illum dolore eu feugiat nulla facilisis at vero eros et luptatum zzril delenit augue duis dolore te feugait nulla facilisi.</p>
  <div class="label__code-box"></div>
  <div class="brand-name">Sola Vie</div>
  <div class="brand-rule"></div>
  <div class="product-type">CREAM</div>
  <div class="facts">
    <div class="facts__title">Nutrition Facts/Datos de Nutrición</div>
    <div class="facts__meta">4 servings per container/4 raciones por envase</div>
    <div class="facts__row facts__row--serving"><span>Serving size/Tamaño de la porción</span><span>1 cup/1 taza (180g)</span></div>
    <div class="facts__meta facts__meta--small">Amount per serving/Cantidad por porción</div>
    <div class="facts__row facts__row--calories"><span>Calories/Calorías</span><span>245</span></div>
    <div class="facts__dv">% Daily Value*/% Valor diario*</div>
    <div class="facts__row facts__row--line facts__row--bold"><span>Total Fat/Grasa total 12g</span><span>14%</span></div>
    <div class="facts__row facts__row--line facts__row--indent"><span>Saturated Fat/Grasa Saturada 2g</span><span>10%</span></div>
    <div class="facts__row facts__row--line facts__row--indent"><span>Trans Fat/Grasa Trans 0g</span><span></span></div>
    <div class="facts__row facts__row--line facts__row--bold"><span>Cholesterol/Colesterol 8mg</span><span>3%</span></div>
    <div class="facts__row facts__row--line facts__row--bold"><span>Sodium/Sodio 210mg</span><span>9%</span></div>
    <div class="facts__row facts__row--line facts__row--bold"><span>Total Carbohydrate/Carbohidrato Total 34g</span><span>12%</span></div>
    <p class="facts__note">*The % Daily Value (DV) tells you how much a nutrient in a serving of food adds to a daily diet. 2,000 calories a day is used for general advice.</p>
    <p class="facts__note">*El % Valor Diario indica cuánto aporta un nutriente de una porción a una dieta diaria de 2,000 calorías.</p>
  </div>
  <p class="label__tagline">Lorem ipsum amet, consectetuer adipiscing elit,<br>tincidunt ut laoreet dolore magna aliquam erat volutpat.</p>
</section>

</body>
</html>
```